Freelance Makeup Artist Needing Business Card Design

I am a freelance makeup artist looking for a design for my business cards.
My target audience is people looking for bridal makeup, so i was thinking minimalistic style, black with white or gold foil accents.
Something that feels classy but simple and to the point.

I would like the front to state Naomi Carrow and Makeup Artist, and the back to include my social media and contact details.

Target Market(s)

Brides, young women

Industry/Entity Type

Business

Contact Information for Business Card

0417293846
naomi.carrow@mailvista.com
www.snapgrid.com/naomi.carrow
www.friendpage.com/NaomiCarrowMakeup

Requirements
Nice to have
• Social media icons next to relevant contact details

```html
<!DOCTYPE html>
<html lang="en">
<head>
<meta charset="utf-8">
<title>Naomi Carrow – Makeup Artist Business Card</title>
<link href="https://fonts.googleapis.com/css2?family=Mr+Dafoe&family=Cinzel:wght@500;600&family=Montserrat:wght@500&display=swap" rel="stylesheet">
<style>
  :root {
    --backdrop: #8cc9cb;
    --card: #1c1c1c;
    --gold: #c98b52;
    --gold-light: #e0a56b;
  }
  * { margin: 0; padding: 0; box-sizing: border-box; }
  html, body { width: 1200px; height: 1144px; overflow: hidden; }
  body { background: var(--backdrop); position: relative; }

  .card {
    position: absolute;
    left: 277px;
    width: 616px;
    height: 356px;
    background: var(--card);
    color: var(--gold);
  }
  .card--front { top: 114px; }
  .card--back { top: 613px; }

  .signature {
    position: absolute;
    left: 0; right: 0;
    text-align: center;
    font-family: "Mr Dafoe", cursive;
    color: var(--gold-light);
    line-height: 1;
    white-space: nowrap;
  }
  .role {
    position: absolute;
    left: 0; right: 0;
    text-align: center;
    font-family: "Cinzel", serif;
    font-weight: 600;
    color: var(--gold-light);
    white-space: nowrap;
  }
  .card--front .signature { top: 100px; font-size: 82px; }
  .card--front .role { top: 216px; font-size: 25px; letter-spacing: 7px; }
  .card--back .signature { top: 28px; font-size: 52px; }
  .card--back .role { top: 86px; font-size: 15px; letter-spacing: 4px; }

  .contact {
    position: absolute;
    display: flex;
    align-items: center;
    gap: 12px;
    font-family: "Montserrat", sans-serif;
    font-weight: 500;
    color: var(--gold);
    white-space: nowrap;
  }
  .contact--social { left: 0; right: 0; justify-content: center; font-size: 16px; }
  .contact--snapgrid { top: 134px; }
  .contact--friendpage { top: 174px; }
  .contact--email { top: 298px; left: 65px; font-size: 14px; gap: 10px; }
  .contact--phone { top: 298px; right: 70px; font-size: 14px; gap: 12px; }

  .mark-circle { width: 26px; height: 26px; border: 2px solid var(--gold); border-radius: 50%; }
  .mark-square { width: 26px; height: 26px; background: var(--gold); }

  .divider {
    position: absolute;
    top: 241px;
    left: 112px;
    width: 388px;
    height: 1px;
    background: var(--gold);
  }
</style>
</head>
<body>
  <section class="card card--front">
    <h1 class="signature">Naomi Carrow</h1>
    <p class="role">Makeup Artist</p>
  </section>

  <section class="card card--back">
    <h2 class="signature">Naomi Carrow</h2>
    <p class="role">Makeup Artist</p>

    <div class="contact contact--social contact--snapgrid">
      <span class="mark-circle"></span>
      <span>www.snapgrid.com/naomi.carrow</span>
    </div>
    <div class="contact contact--social contact--friendpage">
      <span class="mark-square"></span>
      <span>www.friendpage.com/NaomiCarrowMakeup</span>
    </div>

    <div class="divider"></div>

    <div class="contact contact--email">
      <svg width="22" height="16" viewBox="0 0 22 16" fill="none" stroke="#c98b52" stroke-width="1.5">
        <rect x="1" y="1" width="20" height="14"/>
        <path d="M1 1 L11 9 L21 1"/>
        <path d="M1 15 L8 7 M21 15 L14 7"/>
      </svg>
      <span>naomi.carrow@mailvista.com</span>
    </div>

    <div class="contact contact--phone">
      <svg width="22" height="22" viewBox="0 0 24 24" fill="#c98b52">
        <path d="M6.6 10.8c1.4 2.8 3.8 5.1 6.6 6.6l2.2-2.2c.3-.3.7-.4 1-.2 1.1.4 2.3.6 3.6.6.6 0 1 .4 1 1V20c0 .6-.4 1-1 1C10.6 21 3 13.4 3 4c0-.6.4-1 1-1h3.5c.6 0 1 .4 1 1 0 1.3.2 2.5.6 3.6.1.3 0 .7-.2 1L6.6 10.8z"/>
      </svg>
      <span>0417293846</span>
    </div>
  </section>
</body>
</html>
```